Business card for partnership

Plumbing and hvac company needing a minimal business card. We already have a logo i would like the front of the card just the logo and the back have all info.

Target Market(s)

Commercial facilities

Industry/Entity Type

Plumbing hvac

Contact Information for Business Card

We would like it double sided. Logo big and bold on the front and out info on the back. Our info on back would be name and position phone, email, and location

```html
<!DOCTYPE html>
<html lang="en">
<head>
<meta charset="utf-8">
<title>Keystone Mechanical – Business Card</title>
<link rel="stylesheet" href="https://fonts.googleapis.com/css2?family=Open+Sans:wght@400;700&display=swap">
<style>
  :root {
    --page-bg: #e4e1dc;
    --card-navy: #3f5366;
    --card-navy-light: #475c70;
    --accent-orange: #e8661c;
    --deco-brown: #6e5553;
    --text-white: #f4f4f4;
    --text-soft: #d9dee3;
  }
  * { box-sizing: border-box; margin: 0; padding: 0; }
  html, body {
    width: 1200px; height: 900px; overflow: hidden;
    background: var(--page-bg);
    font-family: "Open Sans", Arial, sans-serif;
  }
  .sheet {
    width: 1200px; height: 900px;
    display: flex; flex-direction: column; align-items: center; justify-content: center;
    gap: 44px;
  }
  .card {
    position: relative;
    width: 640px; height: 366px;
    background: linear-gradient(100deg, var(--card-navy) 0%, var(--card-navy-light) 100%);
    overflow: hidden;
    box-shadow: 0 6px 18px rgba(0,0,0,.18);
  }
  .card__deco {
    position: absolute;
    left: 120px; bottom: -150px;
    width: 300px; height: 300px;
    border-radius: 50%;
    background: linear-gradient(160deg, var(--deco-brown), rgba(110,85,83,.55));
    opacity: .85;
  }
  .brand {
    position: absolute;
    display: flex; align-items: center; gap: 12px;
    color: var(--text-white);
    font-weight: 700;
    text-transform: uppercase;
    letter-spacing: .04em;
    line-height: 1;
  }
  .brand__mark {
    width: 22px; height: 22px;
    background: var(--accent-orange);
    flex: none;
  }
  /* info side */
  .person { position: absolute; left: 40px; top: 38px; }
  .person__role { color: var(--text-soft); font-size: 14px; }
  .person__name {
    color: var(--accent-orange); font-size: 17px; font-weight: 700;
    letter-spacing: .04em; text-transform: uppercase;
  }
  .contact {
    position: absolute; left: 330px; top: 150px; width: 290px;
    list-style: none;
    color: var(--text-white); font-size: 14px;
  }
  .contact__item { display: flex; align-items: center; gap: 9px; margin-bottom: 6px; }
  .contact__icon { width: 13px; height: 13px; flex: none; fill: var(--accent-orange); }
  .contact__rule {
    position: absolute; left: 330px; top: 216px; width: 310px;
    height: 1px; background: var(--accent-orange);
  }
  .card--info .brand { left: 330px; top: 244px; font-size: 30px; }
  /* logo side */
  .card--logo .brand { left: 230px; top: 88px; font-size: 40px; }
</style>
</head>
<body>
<main class="sheet">
  <section class="card card--info" aria-label="Card back with contact details">
    <div class="card__deco" role="img" aria-label="Faint brand symbol decoration"></div>
    <div class="person">
      <p class="person__role">Owner</p>
      <p class="person__name">Daniel Marsh</p>
    </div>
    <ul class="contact">
      <li class="contact__item">
        <svg class="contact__icon" viewBox="0 0 24 24" aria-hidden="true"><path d="M6.6 10.8a15.1 15.1 0 0 0 6.6 6.6l2.2-2.2a1 1 0 0 1 1-.25 11.4 11.4 0 0 0 3.6.57 1 1 0 0 1 1 1V20a1 1 0 0 1-1 1A17 17 0 0 1 3 4a1 1 0 0 1 1-1h3.5a1 1 0 0 1 1 1c0 1.25.2 2.45.57 3.57a1 1 0 0 1-.25 1z"/></svg>
        <span>555-014-2280</span>
      </li>
      <li class="contact__item">
        <svg class="contact__icon" viewBox="0 0 24 24" aria-hidden="true"><path d="M3 5h18v14H3z M3 5l9 7 9-7" fill="none" stroke="#e8661c" stroke-width="2.4"/></svg>
        <span>dmarsh@keystonemechanical.biz</span>
      </li>
    </ul>
    <div class="contact__rule"></div>
    <div class="brand"><span class="brand__mark"></span><span>Keystone Mechanical</span></div>
  </section>

  <section class="card card--logo" aria-label="Card front with company name">
    <div class="card__deco" role="img" aria-label="Faint brand symbol decoration"></div>
    <div class="brand"><span class="brand__mark"></span><span>Keystone<br>Mechanical</span></div>
  </section>
</main>
</body>
</html>
```